6" x 11" Print Mailer selling Fiber Internet Services

We need to design a 6" x 11" mailer offering Fiber Internet Services. People receiving this mailer are targeted specifically because fiber has been deployed in their neighborhoods and they can now sign up for fiber service to their door.

We want to lead with "Fiber is now at your door" to hammer home the fact that they can have fiber internet. The picture on the front should be a colorful set of fiber optic cables, the back side can be a happy family using a laptop or some device

We want to advertise two plans:

1) 250 Mbps for $34.95/mo
2) 1 Gbps for $46.95/mo

We need a small but obvious disclaimer that says "Plus $30 Meridel fees"

We want to offer a free month of service for signing up when they mention this mailer and to advertise our 24/7 Technical Support and No Long Term Commitments

We want our Logo (attached) phone number and website visible clearly on the front and back

555-372-9046
www.brovanet.example

Target Market(s)

Residential Households that have fiber internet services now available

Industry/Entity Type

Internet Service Provider

Font styles to use
Serif
Sans Serif
Other font styles liked:
• Futurona is the name of the font in our logo

Requirements
Must have
• Room for the NPDS to print the postage and address on the back. You can use this link for specific requirements from npds: https://about.npds-example.org/guides/g412/g412_003.htm
Nice to have
• Base the color scheme around our logo colors. This can be a vertical or horizontal (or vertical one side, horizontal on the other)
Should not have
• Do not replicate the mailer I have attached, we want something new - it is there for reference.

```html
<!DOCTYPE html>
<html lang="en">
<head>
<meta charset="utf-8">
<title>Brovanet Fiber Mailer</title>
<link rel="stylesheet" href="https://fonts.googleapis.com/css2?family=Poppins:wght@400;500;600;700;800;900&display=swap">
<style>
  :root {
    --backdrop: #5f6468;
    --brand-blue: #2188cc;
    --brand-light: #8bbfe6;
    --deep-blue: #1d5fae;
    --sun-top: #ffd60a;
    --sun-bottom: #f7b500;
    --paper: #ffffff;
  }
  * { margin: 0; padding: 0; box-sizing: border-box; }
  html, body {
    width: 789px; height: 1200px; overflow: hidden;
    background: var(--backdrop);
    font-family: "Poppins", sans-serif;
  }
  .mailer {
    position: absolute; left: 124px; top: 104px;
    width: 540px; height: 990px;
    background: var(--paper);
    overflow: hidden;
  }
  .family-photo {
    position: absolute; inset: 0 0 auto 0; height: 530px;
    clip-path: polygon(0 0, 100% 0, 100% 526px, 0 218px);
    background: linear-gradient(160deg, #e3e8ea 0%, #c9b4a6 38%, #7d8fa3 70%, #4b6684 100%);
  }
  .logo {
    position: absolute; left: 382px; top: 16px;
    display: flex; align-items: center; gap: 6px;
    color: #4aa3e0; font-weight: 500; font-size: 27px; letter-spacing: -0.5px;
  }
  .logo-dot { width: 12px; height: 12px; border-radius: 50%; background: #4aa3e0; }
  .offers { position: absolute; inset: 0; }
  .headline {
    position: absolute; left: 0; width: 540px; text-align: center;
    color: var(--brand-blue); font-weight: 900; line-height: 1;
  }
  .headline-fiber { top: 502px; font-size: 136px; letter-spacing: -2px; }
  .headline-now { top: 626px; font-size: 70px; color: var(--brand-light); letter-spacing: -2px; }
  .headline-door { top: 686px; font-size: 62px; letter-spacing: -2px; }
  .divider {
    position: absolute; left: 129px; top: 760px; width: 280px; height: 5px;
    background: var(--brand-light);
  }
  .support {
    position: absolute; left: 0; width: 540px; text-align: center;
    color: var(--brand-blue); font-weight: 800; line-height: 1;
  }
  .support-hours { top: 776px; font-size: 43px; letter-spacing: -2px; }
  .support-word { top: 816px; font-size: 66px; letter-spacing: -1px; }
  .commitments {
    position: absolute; left: 81px; top: 880px; width: 380px; height: 36px;
    background: var(--brand-blue); color: var(--paper);
    font-weight: 800; font-size: 21px; letter-spacing: -0.5px;
    display: flex; align-items: center; justify-content: center;
  }
  .contact-bar {
    position: absolute; left: 0; bottom: 0; width: 540px; height: 44px;
    background: var(--brand-blue); color: var(--paper);
    font-weight: 500; font-size: 19px; white-space: nowrap;
  }
  .contact-item { position: absolute; top: 0; height: 44px; display: flex; align-items: center; gap: 12px; }
  .contact-phone { left: 38px; }
  .contact-web { right: 28px; gap: 12px; }
  .contact-icon {
    width: 23px; height: 23px; border-radius: 4px; background: var(--paper);
    display: flex; align-items: center; justify-content: center; flex: none;
  }
</style>
</head>
<body>
<main class="mailer">
  <div class="family-photo" role="img" aria-label="Smiling family of three looking at a laptop together in a bright living room"></div>

  <div class="logo"><span class="logo-dot"></span>Brovanet</div>

  <svg class="offers" width="540" height="990" viewBox="0 0 540 990">
    <line x1="0" y1="218" x2="540" y2="526" stroke="var(--brand-light)" stroke-width="5"/>

    <g class="plan plan-250">
      <polygon points="115,210 177,245 177,314 115,348 53,314 53,245" fill="var(--brand-blue)" stroke="var(--brand-light)" stroke-width="3"/>
      <text x="120" y="260" text-anchor="middle" fill="#fff" font-family="Poppins, sans-serif" font-weight="500" font-size="14.5">250 Mbps for</text>
      <text x="61" y="292" fill="#fff" font-family="Poppins, sans-serif" font-weight="700" font-size="16">$</text>
      <text x="71" y="295" fill="#fff" font-family="Poppins, sans-serif" font-weight="800" font-size="42" letter-spacing="-1">34.</text>
      <text x="137" y="279" fill="#fff" font-family="Poppins, sans-serif" font-weight="800" font-size="22">95</text>
      <text x="140" y="291" fill="#fff" font-family="Poppins, sans-serif" font-weight="600" font-size="7.5">/month</text>
      <text x="115" y="306" text-anchor="middle" fill="#fff" font-family="Poppins, sans-serif" font-weight="500" font-size="6">Plus $30 Meridel fees</text>
    </g>

    <g class="free-month">
      <defs>
        <linearGradient id="sun" x1="0" y1="0" x2="0" y2="1">
          <stop offset="0" stop-color="var(--sun-top)"/>
          <stop offset="1" stop-color="var(--sun-bottom)"/>
        </linearGradient>
      </defs>
      <polygon points="270,299 332,333 332,401 270,435 208,401 208,333" fill="url(#sun)" stroke="var(--brand-light)" stroke-width="3"/>
      <text x="270" y="356" text-anchor="middle" fill="var(--deep-blue)" font-family="Poppins, sans-serif" font-weight="900" font-size="28" textLength="80" lengthAdjust="spacingAndGlyphs">FIRST</text>
      <text x="270" y="374" text-anchor="middle" fill="var(--deep-blue)" font-family="Poppins, sans-serif" font-weight="900" font-size="21" textLength="80" lengthAdjust="spacingAndGlyphs">MONTH</text>
      <text x="270" y="398" text-anchor="middle" fill="var(--deep-blue)" font-family="Poppins, sans-serif" font-weight="900" font-size="31" textLength="80" lengthAdjust="spacingAndGlyphs">FREE</text>
      <text x="270" y="406" text-anchor="middle" fill="var(--deep-blue)" font-family="Poppins, sans-serif" font-weight="700" font-size="4.2" textLength="78" lengthAdjust="spacingAndGlyphs">WHEN YOU MENTION THIS MAILER</text>
    </g>

    <g class="plan plan-1g" transform="translate(301,175)">
      <polygon points="115,210 177,245 177,314 115,348 53,314 53,245" fill="var(--brand-blue)" stroke="var(--brand-light)" stroke-width="3"/>
      <text x="120" y="260" text-anchor="middle" fill="#fff" font-family="Poppins, sans-serif" font-weight="500" font-size="16">1 Gbps for</text>
      <text x="61" y="292" fill="#fff" font-family="Poppins, sans-serif" font-weight="700" font-size="16">$</text>
      <text x="71" y="295" fill="#fff" font-family="Poppins, sans-serif" font-weight="800" font-size="42" letter-spacing="-1">46.</text>
      <text x="137" y="279" fill="#fff" font-family="Poppins, sans-serif" font-weight="800" font-size="22">95</text>
      <text x="140" y="291" fill="#fff" font-family="Poppins, sans-serif" font-weight="600" font-size="7.5">/month</text>
      <text x="115" y="306" text-anchor="middle" fill="#fff" font-family="Poppins, sans-serif" font-weight="500" font-size="6">Plus $30 Meridel fees</text>
    </g>
  </svg>

  <h1>
    <span class="headline headline-fiber">FIBER</span>
    <span class="headline headline-now">IS NOW AT</span>
    <span class="headline headline-door">YOUR DOOR</span>
  </h1>
  <div class="divider"></div>
  <p class="support support-hours">24/7 TECHNICAL</p>
  <p class="support support-word">SUPPORT</p>
  <p class="commitments">NO LONG TERM COMMITMENTS</p>

  <footer class="contact-bar">
    <div class="contact-item contact-phone">
      <span class="contact-icon">
        <svg width="15" height="15" viewBox="0 0 24 24"><path d="M6.6 10.8a15.1 15.1 0 0 0 6.6 6.6l2.2-2.2a1 1 0 0 1 1-.25 11.4 11.4 0 0 0 3.6.57 1 1 0 0 1 1 1V20a1 1 0 0 1-1 1A17 17 0 0 1 3 4a1 1 0 0 1 1-1h3.5a1 1 0 0 1 1 1 11.4 11.4 0 0 0 .57 3.6 1 1 0 0 1-.25 1z" fill="var(--brand-blue)"/></svg>
      </span>
      555-372-9046
    </div>
    <div class="contact-item contact-web">
      <span class="contact-icon">
        <svg width="15" height="15" viewBox="0 0 24 24" fill="none" stroke="var(--brand-blue)" stroke-width="2.4" stroke-linecap="round"><path d="M10 14a4 4 0 0 0 5.7 0l3-3a4 4 0 0 0-5.7-5.7l-1 1"/><path d="M14 10a4 4 0 0 0-5.7 0l-3 3a4 4 0 0 0 5.7 5.7l1-1"/></svg>
      </span>
      www.brovanet.example
    </div>
  </footer>
</main>
</body>
</html>
```